Unusual Options Activity Graphic Card Design for Finance App

We are developing a financial data platform called Vantix Pulse, and we need a visually striking, mobile-optimized graphic card design to display unusual options activity. The card will be featured in our mobile app and marketing materials, inspired by platforms like Marlocq and Pindrake Lane.
🔹 Design Goals:
Modern, clean, and professional aesthetic
Use vibrant electric blue, green, or dark theme gradients
Must feel tech-savvy and finance-oriented
Layout should be optimized for vertical mobile format (portrait)
🔹 Information to Include in the Card:
Ticker Symbol (e.g., QZR) with colored badge
Date & Time of trade
Trade Type (e.g., Sweep Call / Put)
Execution Type (At Ask or At Bid)
Strike Price
Expiration Date
Premium (e.g., $342.75K)
Size@Price (e.g., 6995@$0.49)
Volume
Open Interest
Branding at bottom: “Vantix Pulse” in modern font
🔹 Inspiration:
Marlocq’s profit/loss cards
Clean fintech dashboards (Quillmere, Pindrake Lane, Haskvorn Console)
Please provide the final deliverable in high-resolution PNG and layered PSD or Figma file for future edits.
Stock Market Traders
Finance

```html
<!DOCTYPE html>
<html lang="en">
<head>
<meta charset="utf-8">
<title>Unusual Options Activity – Card Design</title>
<link href="https://fonts.googleapis.com/css2?family=Inter:wght@400;500;600;700;800;900&display=swap" rel="stylesheet">
<style>
:root{
  --bg:#04081a;
  --ink:#ffffff;
  --muted:#9aa6b8;
  --green:#4cc35a;
  --red:#e0413f;
  --card-a:#21503c;
  --card-b:#1f3f4c;
  --card-c:#1c2d58;
  --screen:#0b0d12;
  --field:#2b2f38;
  --chrome:#d9dadf;
}
*{box-sizing:border-box;margin:0;padding:0}
html,body{width:1200px;height:975px;overflow:hidden;background:var(--bg)}
body{position:relative;font-family:"Inter",sans-serif;color:var(--ink)}
.abs{position:absolute}

.board-title{left:60px;top:34px;width:280px;text-align:center;font-weight:800;font-size:21px;line-height:24.5px;letter-spacing:-.4px}
.cursor{left:259px;top:115px}

.note{font-weight:700;font-size:14px;letter-spacing:-.2px}
.arrows{left:0;top:0;pointer-events:none}

/* option card */
.card{position:absolute;width:126px;height:101px;border-radius:4px;padding:8px 9px 0;
  background:linear-gradient(155deg,var(--card-a) 0%,var(--card-b) 55%,var(--card-c) 100%);overflow:hidden}
.card-head{display:flex;height:11px;border:.7px solid rgba(255,255,255,.85);border-radius:2px;overflow:hidden;width:109px}
.tick{display:flex;align-items:center;justify-content:center;width:22px;font-size:6.4px;font-weight:700;color:#0b1a10}
.tick.up{background:var(--green)}
.tick.down{background:var(--red);color:#2a0808}
.stamp{flex:1;display:flex;align-items:center;justify-content:center;font-size:7px;font-weight:500}
.card-type{display:flex;justify-content:space-between;align-items:center;margin-top:7px}
.card-type h3{font-size:7px;font-weight:700;letter-spacing:.1px}
.call{color:var(--green)}
.put{color:var(--red)}
.exec{font-size:4.4px;font-weight:500;margin-right:14px}
.exec.ask{color:var(--green)}
.exec.bid{color:var(--red)}
.card-data{display:grid;grid-template-columns:36px 41px 1fr;row-gap:3px;margin-top:4px}
.card-data div{display:flex;flex-direction:column}
.card-data dt{font-size:3.4px;color:var(--muted);letter-spacing:.2px;text-transform:uppercase}
.card-data dd{font-size:5.4px;font-weight:700;margin-top:1px}
.card-brand{position:absolute;left:9px;right:9px;top:81px;border-top:.6px solid rgba(255,255,255,.2);
  display:flex;justify-content:center;align-items:center;gap:3px;padding-top:5px;font-size:6.6px;font-weight:800;letter-spacing:.2px}
.card-brand i{width:6px;height:6px;border-radius:50%;background:var(--green)}

/* large card */
.card.tall{width:128px;height:170px;padding:9px 11px 0}
.tall .card-head{width:105px}
.tall h2{font-size:16px;font-weight:700;margin-top:9px;letter-spacing:.2px;white-space:nowrap}
.tall .exec-big{font-size:8px;color:var(--green);margin-top:1px}
.tall .card-data{grid-template-columns:53px 1fr;row-gap:5px;margin-top:7px}
.tall .card-data dt{font-size:5.2px;text-transform:uppercase}
.tall .card-data dd{font-size:8px;font-weight:600}
.tall .card-brand{top:146px;left:11px;right:11px;border:none}

/* screens */
.screen-label{font-weight:700;font-size:17px}
.screen{position:absolute;overflow:hidden;border-radius:8px;background:var(--screen)}
.status{display:flex;justify-content:space-between;align-items:center;font-size:7px;font-weight:600;padding:0 20px}
.status .bars{display:flex;gap:3px;align-items:center}
.status .bars i{display:block;width:9px;height:4px;border-radius:1px;background:currentColor}
.app-title{text-align:center;font-size:8px;margin-top:12px}
.tabs{display:flex;gap:12px;font-size:5.2px;padding-left:6px;margin-top:8px;white-space:nowrap;color:#e6e6e6}
.tabs .on{color:var(--green)}
.tab-line{height:.6px;background:#222;margin-top:6px}
.app-nav{position:absolute;left:0;right:0;bottom:0;height:34px;background:var(--screen);display:flex;justify-content:space-around;padding-top:6px;font-size:4.6px;color:#bbb}
.app-nav span{display:flex;flex-direction:column;align-items:center;gap:2px}
.app-nav i{display:block;width:6px;height:6px;background:#9aa;border-radius:1px}
.app-nav .on{color:var(--green)}
.app-nav .on i{background:var(--green);height:3px;margin-top:2px}
.homebar{position:absolute;bottom:4px;left:50%;width:60px;height:2px;margin-left:-30px;border-radius:2px;background:#ddd}

.web .status{background:#fff;color:#000;height:24px}
.web-top{display:flex;align-items:center;height:34px;padding:0 8px 0 2px;font-size:6px;font-weight:500;background:#121418}
.web-top .dot{width:12px;height:12px;border-radius:50%;border:1.4px solid var(--green);margin-right:8px}
.web-top .toggle{margin-left:auto;width:22px;height:10px;border-radius:6px;background:#fff;position:relative}
.web-top .toggle::before{content:"";position:absolute;left:1px;top:1px;width:8px;height:8px;border-radius:50%;background:#111}
.web-top .avatar{width:11px;height:11px;border-radius:50%;background:linear-gradient(135deg,#cfd3da,#6d737e);margin:0 6px 0 7px}
.web-top .menu{width:6px;height:4px;border-top:.8px solid #ccc;border-bottom:.8px solid #ccc;margin-left:8px}
.web h4{font-size:7.5px;font-weight:500;margin:11px 0 0 4px}
.refresh{display:flex;align-items:center;gap:5px;font-size:5px;margin:8px 0 0 5px}
.refresh i{width:11px;height:5px;border-radius:3px;background:#fff;position:relative}
.refresh i::before{content:"";position:absolute;left:.5px;top:.5px;width:4px;height:4px;border-radius:50%;background:#111}
.search{margin:9px 6px 0 4px;height:14px;border-radius:2px;background:var(--field);font-size:5px;color:#aaa;padding:4px 6px}
.tools{display:flex;gap:8px;font-size:4.8px;margin:8px 0 0 13px}
.browser{position:absolute;left:0;right:0;bottom:0;height:48px;background:var(--chrome)}
.url{margin:5px 12px 0;height:14px;border-radius:6px;background:#eceef2;color:#222;font-size:5.6px;display:flex;justify-content:center;align-items:center}
.bnav{display:flex;justify-content:space-around;margin-top:6px;color:#2a7bea;font-size:8px}

.thanks{left:820px;top:840px;width:410px;text-align:center;font-weight:800;font-size:43px;letter-spacing:-1.5px}
.feedback{left:860px;top:902px;width:330px;text-align:center;font-size:16px;line-height:19px;font-weight:400}
</style>
</head>
<body>

<h1 class="abs board-title">Unusual Options Activity :<br>Graphic Card Design for<br>Finance App</h1>
<svg class="abs cursor" width="16" height="16" viewBox="0 0 16 16"><path d="M2 1 L14 7 L8 8.5 L5 14 Z" fill="#fff"/></svg>

<!-- annotations -->
<div class="abs note" style="left:87px;top:241px">Ticker Symbol</div>
<div class="abs note" style="left:103px;top:259px">Trade Type</div>
<div class="abs note" style="left:412px;top:233px">Date &amp; Time of trade</div>
<div class="abs note" style="left:412px;top:254px">Execution Type</div>
<div class="abs note" style="left:393px;top:310px">Branding</div>
<svg class="abs arrows" width="1200" height="975">
  <defs><marker id="head" markerWidth="6" markerHeight="6" refX="5" refY="3" orient="auto"><path d="M0 0 L6 3 L0 6 Z" fill="#fff"/></marker></defs>
  <g fill="none" stroke="#fff" stroke-width="1" marker-end="url(#head)">
    <path d="M185 249 Q206 228 231 244"/>
    <path d="M181 268 Q202 258 229 264"/>
    <path d="M407 243 Q380 228 352 243"/>
    <path d="M404 263 Q375 250 348 263"/>
    <path d="M383 322 Q365 302 338 321"/>
  </g>
  <g fill="#fff"><circle cx="185" cy="249" r="2"/><circle cx="181" cy="268" r="2"/><circle cx="407" cy="243" r="2"/><circle cx="404" cy="263" r="2"/><circle cx="383" cy="322" r="2"/></g>
</svg>

<article class="card" style="left:228px;top:230px">
  <header class="card-head"><span class="tick up">QZR</span><span class="stamp">04/05/25 | 10:32:12</span></header>
  <div class="card-type"><h3>TRADE <span class="call">CALL</span></h3><span class="exec ask">AT ASk</span></div>
  <dl class="card-data"><div><dt>Strike</dt><dd>$91</dd></div><div><dt>Expiration</dt><dd>19 Apr 25</dd></div><div><dt>Open interest</dt><dd>2424</dd></div><div><dt>Premium</dt><dd>$342.75K</dd></div><div><dt>Size@price</dt><dd>6995@$0.49</dd></div><div><dt>Volume</dt><dd>34.7K</dd></div></dl>
  <footer class="card-brand"><i></i>Vantix Pulse</footer>
</article>

<!-- variant grid -->
<article class="card" style="left:630px;top:222px">
  <header class="card-head"><span class="tick up">QZR</span><span class="stamp">04/05/25 | 10:32:12</span></header>
  <div class="card-type"><h3>SWEEP <span class="put">PUT</span></h3><span class="exec ask">AT ASk</span></div>
  <dl class="card-data"><div><dt>Strike</dt><dd>$91</dd></div><div><dt>Expiration</dt><dd>19 Apr 25</dd></div><div><dt>Open interest</dt><dd>2424</dd></div><div><dt>Premium</dt><dd>$342.75K</dd></div><div><dt>Size@price</dt><dd>6995@$0.49</dd></div><div><dt>Volume</dt><dd>34.7K</dd></div></dl>
  <footer class="card-brand"><i></i>Vantix Pulse</footer>
</article>
<article class="card" style="left:782px;top:222px">
  <header class="card-head"><span class="tick up">QZR</span><span class="stamp">04/05/25 | 10:32:12</span></header>
  <div class="card-type"><h3>TRADE <span class="call">CALL</span></h3><span class="exec bid">AT BID</span></div>
  <dl class="card-data"><div><dt>Strike</dt><dd>$91</dd></div><div><dt>Expiration</dt><dd>19 Apr 25</dd></div><div><dt>Open interest</dt><dd>2424</dd></div><div><dt>Premium</dt><dd>$342.75K</dd></div><div><dt>Size@price</dt><dd>6995@$0.49</dd></div><div><dt>Volume</dt><dd>34.7K</dd></div></dl>
  <footer class="card-brand"><i></i>Vantix Pulse</footer>
</article>
<article class="card" style="left:934px;top:222px">
  <header class="card-head"><span class="tick up">QZR</span><span class="stamp">04/05/25 | 10:32:12</span></header>
  <div class="card-type"><h3>TRADE <span class="put">PUT</span></h3><span class="exec ask">AT ASk</span></div>
  <dl class="card-data"><div><dt>Strike</dt><dd>$91</dd></div><div><dt>Expiration</dt><dd>19 Apr 25</dd></div><div><dt>Open interest</dt><dd>2424</dd></div><div><dt>Premium</dt><dd>$342.75K</dd></div><div><dt>Size@price</dt><dd>6995@$0.49</dd></div><div><dt>Volume</dt><dd>34.7K</dd></div></dl>
  <footer class="card-brand"><i></i>Vantix Pulse</footer>
</article>
<article class="card" style="left:630px;top:339px">
  <header class="card-head"><span class="tick down">QZR</span><span class="stamp">04/05/25 | 10:32:12</span></header>
  <div class="card-type"><h3>TRADE <span class="put">PUT</span></h3><span class="exec ask">AT ASk</span></div>
  <dl class="card-data"><div><dt>Strike</dt><dd>$91</dd></div><div><dt>Expiration</dt><dd>19 Apr 25</dd></div><div><dt>Open interest</dt><dd>2424</dd></div><div><dt>Premium</dt><dd>$342.75K</dd></div><div><dt>Size@price</dt><dd>6995@$0.49</dd></div><div><dt>Volume</dt><dd>34.7K</dd></div></dl>
  <footer class="card-brand"><i></i>Vantix Pulse</footer>
</article>
<article class="card" style="left:782px;top:339px">
  <header class="card-head"><span class="tick down">QZR</span><span class="stamp">04/05/25 | 10:32:12</span></header>
  <div class="card-type"><h3>TRADE <span class="call">CALL</span></h3><span class="exec bid">AT BID</span></div>
  <dl class="card-data"><div><dt>Strike</dt><dd>$91</dd></div><div><dt>Expiration</dt><dd>19 Apr 25</dd></div><div><dt>Open interest</dt><dd>2424</dd></div><div><dt>Premium</dt><dd>$342.75K</dd></div><div><dt>Size@price</dt><dd>6995@$0.49</dd></div><div><dt>Volume</dt><dd>34.7K</dd></div></dl>
  <footer class="card-brand"><i></i>Vantix Pulse</footer>
</article>
<article class="card" style="left:934px;top:339px">
  <header class="card-head"><span class="tick down">QZR</span><span class="stamp">04/05/25 | 10:32:12</span></header>
  <div class="card-type"><h3>TRADE <span class="call">CALL</span></h3><span class="exec ask">AT ASk</span></div>
  <dl class="card-data"><div><dt>Strike</dt><dd>$91</dd></div><div><dt>Expiration</dt><dd>19 Apr 25</dd></div><div><dt>Open interest</dt><dd>2424</dd></div><div><dt>Premium</dt><dd>$342.75K</dd></div><div><dt>Size@price</dt><dd>6995@$0.49</dd></div><div><dt>Volume</dt><dd>34.7K</dd></div></dl>
  <footer class="card-brand"><i></i>Vantix Pulse</footer>
</article>

<!-- app screen -->
<div class="abs screen-label" style="left:158px;top:547px">APP</div>
<section class="screen app" style="left:101px;top:586px;width:164px;height:355px">
  <div class="status" style="height:24px;padding-top:8px"><span>7:09</span><span class="bars"><i></i><i></i></span></div>
  <div class="app-title">Markets</div>
  <nav class="tabs"><span class="on">Option Flow</span><span>Darkpool</span><span>Treemap</span><span>Gamma</span><span>Snaps</span></nav>
  <div class="tab-line"></div>
  <article class="card" style="left:19px;top:68px">
    <header class="card-head"><span class="tick up">QZR</span><span class="stamp">04/05/25 | 10:32:12</span></header>
    <div class="card-type"><h3>TRADE <span class="call">CALL</span></h3><span class="exec ask">AT ASk</span></div>
    <dl class="card-data"><div><dt>Strike</dt><dd>$91</dd></div><div><dt>Expiration</dt><dd>19 Apr 25</dd></div><div><dt>Open interest</dt><dd>2424</dd></div><div><dt>Premium</dt><dd>$342.75K</dd></div><div><dt>Size@price</dt><dd>6995@$0.49</dd></div><div><dt>Volume</dt><dd>34.7K</dd></div></dl>
    <footer class="card-brand"><i></i>Vantix Pulse</footer>
  </article>
  <article class="card" style="left:19px;top:181px">
    <header class="card-head"><span class="tick down">QZR</span><span class="stamp">04/05/25 | 10:32:12</span></header>
    <div class="card-type"><h3>TRADE <span class="call">CALL</span></h3><span class="exec bid">AT ASk</span></div>
    <dl class="card-data"><div><dt>Strike</dt><dd>$91</dd></div><div><dt>Expiration</dt><dd>19 Apr 25</dd></div><div><dt>Open interest</dt><dd>2424</dd></div><div><dt>Premium</dt><dd>$342.75K</dd></div><div><dt>Size@price</dt><dd>6995@$0.49</dd></div><div><dt>Volume</dt><dd>34.7K</dd></div></dl>
    <footer class="card-brand"><i></i>Vantix Pulse</footer>
  </article>
  <article class="card" style="left:19px;top:294px">
    <header class="card-head"><span class="tick up">QZR</span><span class="stamp">04/05/25 | 10:32:12</span></header>
  </article>
  <nav class="app-nav"><span><i></i></span><span><i></i></span><span class="on"><i></i>Markets</span><span><i></i></span><span><i></i></span></nav>
  <div class="homebar"></div>
</section>

<!-- web app screen -->
<div class="abs screen-label" style="left:334px;top:543px">Web APP</div>
<section class="screen web" style="left:290px;top:583px;width:166px;height:358px">
  <div class="status"><span>7:09</span><span class="bars"><i></i><i></i></span></div>
  <div class="web-top"><span class="dot"></span>Option Flow<span class="toggle"></span><span class="avatar" role="img" aria-label="User avatar"></span><span class="menu"></span></div>
  <h4>Option Flow Data</h4>
  <div class="refresh"><i></i>Auto Refresh</div>
  <div class="search">Search Ticker...</div>
  <div class="tools"><span>☰ Filter</span><span>⇪ Export</span></div>
  <article class="card" style="left:20px;top:142px">
    <header class="card-head"><span class="tick up">QZR</span><span class="stamp">04/05/25 | 10:32:12</span></header>
    <div class="card-type"><h3>TRADE <span class="call">CALL</span></h3><span class="exec ask">AT ASk</span></div>
    <dl class="card-data"><div><dt>Strike</dt><dd>$91</dd></div><div><dt>Expiration</dt><dd>19 Apr 25</dd></div><div><dt>Open interest</dt><dd>2424</dd></div><div><dt>Premium</dt><dd>$342.75K</dd></div><div><dt>Size@price</dt><dd>6995@$0.49</dd></div><div><dt>Volume</dt><dd>34.7K</dd></div></dl>
    <footer class="card-brand"><i></i>Vantix Pulse</footer>
  </article>
  <article class="card" style="left:20px;top:255px">
    <header class="card-head"><span class="tick down">QZR</span><span class="stamp">04/05/25 | 10:32:12</span></header>
    <div class="card-type"><h3>TRADE <span class="call">CALL</span></h3><span class="exec bid">AT ASk</span></div>
    <dl class="card-data"><div><dt>Strike</dt><dd>$91</dd></div><div><dt>Expiration</dt><dd>19 Apr 25</dd></div><div><dt>Open interest</dt><dd>2424</dd></div></dl>
  </article>
  <div class="browser">
    <div class="url">🔒 app.vantixpulse.com</div>
    <div class="bnav"><span>‹</span><span style="color:#aab">›</span><span>⇪</span><span>▯</span><span>⧉</span></div>
    <div class="homebar" style="background:#333"></div>
  </div>
</section>

<!-- detail cards -->
<article class="card tall" style="left:664px;top:563px">
  <header class="card-head"><span class="tick up">QZR</span><span class="stamp">04/05/25 | 10:32:12</span></header>
  <h2>TRADE <span class="call">CALL</span></h2>
  <div class="exec-big">AT ASK</div>
  <dl class="card-data"><div><dt>Strike</dt><dd>$91</dd></div><div><dt>Expiration</dt><dd>19 Apr 25</dd></div><div><dt>Premium</dt><dd>$342.75K</dd></div><div><dt>Size@price</dt><dd>6995@$0.49</dd></div><div><dt>Volume</dt><dd>34.7K</dd></div><div><dt>Open interest</dt><dd>2424</dd></div></dl>
  <footer class="card-brand"><i></i>Vantix Pulse</footer>
</article>
<article class="card" style="left:821px;top:571px">
  <header class="card-head"><span class="tick up">QZR</span><span class="stamp">04/05/25 | 10:32:12</span></header>
  <div class="card-type"><h3>TRADE <span class="call">CALL</span></h3><span class="exec ask">AT ASk</span></div>
  <dl class="card-data"><div><dt>Strike</dt><dd>$91</dd></div><div><dt>Expiration</dt><dd>19 Apr 25</dd></div><div><dt>Open interest</dt><dd>2424</dd></div><div><dt>Premium</dt><dd>$342.75K</dd></div><div><dt>Size@price</dt><dd>6995@$0.49</dd></div><div><dt>Volume</dt><dd>34.7K</dd></div></dl>
  <footer class="card-brand"><i></i>Vantix Pulse</footer>
</article>

<div class="abs thanks">Thank you</div>
<p class="abs feedback">Your feedback matters to us. Let us know what you think!</p>

</body>
</html>
```